We are the world's leading center for transgender surgery and have multiple locations.

We want a unique and dynamic business card that wows potential patients and referral sources (physicians, previous patients, etc). We are open to inventive designs, card shape, additional design on the back of the card, etc.

We are a surgical practice in a competitive environment and want to stand out as the leader in transgender surgery. We have multiple surgeons with unique talents who are impeccably trained with extensive experience. We are dedicated to our patients and their needs. We want the card to stand out and impress them. We want it to be suitable to all of the surgeons as well as our staff.

Our practice started as a small practice in San Francisco, CA and now has an additional location in Austin Texas (as well as another city to be announced later). Our practice has plastic surgeons, reconstructive urologists, general surgeons and gynecologists.

We continue to boast some of the lowest published phalloplasty complication rates in the world and our San Francisco microsurgeons that we have been working with for more than a year and a half have 0 microvascular take backs and 0 flap failures. Between our two centers in San Francisco, California and Austin, Texas, we perform 5-6 phalloplasties per week, making us one of the largest volume centers in the world.

Target Market(s)

Potential Transgender patients (all genders) and referring physicians

Industry/Entity Type

Surgeon

Contact Information for Business Card

Here is an example of one of our physicians:

Daniel R. Ostrow, MD
Gender-Affirming Urologic Reconstruction
Diplomate, National Council of Renal Medicine with added qualification in Pelvic and Restorative Care

318 Lady Harriet Moore Ave
Suite 7
Westhaven, CA 94817

phone 628-738-1942
fax 628-582-1947

Font styles to use
Sans Serif

Requirements
Must have
• Must have a unique look, but tasteful.
Nice to have
• ?
Should not have
• ?

```html
<!DOCTYPE html>
<html lang="en">
<head>
<meta charset="utf-8">
<title>Alder Grove Clinic – Business Card</title>
<link href="https://fonts.googleapis.com/css2?family=Exo+2:wght@400;500;600;700&display=swap" rel="stylesheet">
<style>
  :root {
    --magenta: #9b2a6e;
    --navy: #2f3a78;
    --ink: #2a3470;
    --card-white: #ffffff;
    --page: #ece9e4;
    --back-top: #8f2371;
    --back-mid: #6a2a78;
    --back-bottom: #3b2f7c;
    --rule: #3a4483;
  }
  * { box-sizing: border-box; margin: 0; padding: 0; }
  html, body { width: 1200px; height: 923px; overflow: hidden; }
  body {
    background: var(--page);
    font-family: "Exo 2", sans-serif;
    display: flex;
    align-items: center;
    justify-content: center;
    gap: 40px;
  }
  .card {
    width: 540px;
    height: 309px;
    border-radius: 44px 8px 44px 8px;
    position: relative;
    overflow: hidden;
    box-shadow: 0 6px 18px rgba(0,0,0,0.12);
  }
  .card-front { background: var(--card-white); padding: 34px 36px; }
  .brand { display: flex; align-items: center; gap: 10px; }
  .brand-mark {
    width: 20px; height: 20px;
    background: var(--magenta);
  }
  .brand-name {
    font-weight: 600;
    font-size: 26px;
    letter-spacing: 0.5px;
    color: var(--navy);
    line-height: 1;
  }
  .person { margin-top: 30px; }
  .person-name {
    font-weight: 600;
    font-size: 17px;
    color: var(--navy);
    text-transform: uppercase;
    letter-spacing: 0.4px;
  }
  .person-title {
    font-size: 12.5px;
    color: var(--magenta);
    line-height: 1.35;
    margin-top: 4px;
  }
  .contact-row {
    position: absolute;
    left: 36px; right: 36px; bottom: 30px;
    display: flex;
    justify-content: space-between;
    align-items: flex-end;
  }
  .phones {
    border-top: 1px solid var(--rule);
    padding-top: 8px;
    width: 210px;
    font-size: 12.5px;
    color: var(--ink);
    line-height: 1.5;
  }
  .phone-line { display: flex; align-items: center; gap: 8px; }
  .phone-line svg { width: 11px; height: 11px; fill: var(--magenta); }
  .address {
    border-left: 1px solid var(--rule);
    padding-left: 14px;
    font-size: 12.5px;
    color: var(--ink);
    line-height: 1.5;
  }
  .card-back {
    background: linear-gradient(160deg, var(--back-top) 0%, var(--back-mid) 50%, var(--back-bottom) 100%);
    display: flex;
    align-items: center;
    justify-content: center;
  }
  .card-back .brand-mark { background: #ffffff; width: 24px; height: 24px; }
  .card-back .brand-name { color: #ffffff; font-size: 32px; }
</style>
</head>
<body>
  <section class="card card-front">
    <div class="brand">
      <span class="brand-mark"></span>
      <span class="brand-name">Alder Grove Clinic</span>
    </div>
    <div class="person">
      <p class="person-name">Daniel R. Ostrow, MD</p>
      <p class="person-title">Gender-Affirming Urologic Reconstruction<br>
        Diplomate, National Council of Renal Medicine with<br>
        added qualification in Pelvic and Restorative Care</p>
    </div>
    <div class="contact-row">
      <div class="phones">
        <p class="phone-line">
          <svg viewBox="0 0 24 24" aria-hidden="true"><path d="M6.6 10.8a15.1 15.1 0 0 0 6.6 6.6l2.2-2.2a1 1 0 0 1 1-.25 11.4 11.4 0 0 0 3.6.57 1 1 0 0 1 1 1V20a1 1 0 0 1-1 1A17 17 0 0 1 3 4a1 1 0 0 1 1-1h3.5a1 1 0 0 1 1 1c0 1.25.2 2.45.57 3.57a1 1 0 0 1-.25 1z"/></svg>
          628-738-1942
        </p>
        <p class="phone-line">
          <svg viewBox="0 0 24 24" aria-hidden="true"><path d="M6 3h9v5H6zM4 9h16a2 2 0 0 1 2 2v6h-4v4H6v-4H2v-6a2 2 0 0 1 2-2zm4 7v3h8v-3z"/></svg>
          628-582-1947
        </p>
      </div>
      <div class="address">
        <p>318 Lady Harriet Moore Ave</p>
        <p>Suite 7, Westhaven, CA 94817</p>
      </div>
    </div>
  </section>

  <section class="card card-back">
    <div class="brand">
      <span class="brand-mark"></span>
      <span class="brand-name">Alder Grove Clinic</span>
    </div>
  </section>
</body>
</html>
```